Something different!?!?!?.....Real Estate Business Card

**01/02/2016 Update** I have added a QR code. I am liking Black cards with the Corvath Homes on the back so I do not need "Corvath homes" on the front. Please adjust with QR code somewhere without over crowding the card. Thank you!

**12/27/2015 Update** All the submissions are amazing!!! Thank you so much to every single person who has taken the time out of your day. I'm loving the black with the red but still not stuck on anything. The number one thing I would like is for my hair/ picture and everything to flow into the background or look like I'm popping out of the card 3D without a hard choppy line. I did comment on one of the submissions that the picture flowed great. I am looking for something unique as well. I don't know what but I need my card to stand out from every other Corvath Homes agent as well as other companies in the area. They need to remember me by looking at my card. I am looking for a flyer as well that I can send out to introduce myself to the neighborhood. Maybe a happy holidays? Like a postcard looking for buyers and sellers or anyone with questions about the market. That needs to stand out as well and I would like it the same theme as the business card. Again thank you everyone who is taking the time to help me as I am illiterate when it comes to graphic design!!

I need a Business Card and a post card mailer that I can send out to people in the area. I would like to keep the same theme through out but not a must. I am an agent for Corvath Homes so their logo needs to be somewhere I have attached two. I think as long as its red around white Corvath Homes letters I'm good. I have attached a picture of me in the car if someone could take out the background and make it look professional that would be great otherwise I have also attached someone else and myself messed with (I think it looks tacky). I like when the person looks like they're floating in the background.

If like your work I will be needing someone for marketing campaign designs, etc.

Target Market(s)

MN and WI Real Estate Buyers and Sellers

Industry/Entity Type

Real Estate

Contact Information for Business Card

Tessa Brandow
WI & MN Realtor
18632 County Lane 42/88 South
Dunmere, LK 61359
TessaBrandow@CorvathHomes.example
C: 555.204.6181
W:555.862.1947
F: 555.862.4073

Requirements
Must have
• Picture
• Contact Info
• white Corvath Homes letters with a red box
Nice to have
• 3D
Should not have
• Hard lines around picture

```html
<!DOCTYPE html>
<html lang="en">
<head>
<meta charset="utf-8">
<title>Tessa Brandow – Business Card</title>
<link rel="stylesheet" href="https://fonts.googleapis.com/css2?family=Questrial&family=Arimo:wght@400;700&display=swap">
<style>
  :root {
    --page: #e9e7e4;
    --card-black: #141414;
    --card-black-soft: #2a2a2a;
    --white: #ffffff;
    --red: #b3202e;
    --red-deep: #8e1622;
    --grey-name: #6e6e70;
    --grey-light: #c9c9cb;
    --photo-dark: #2b1d17;
    --photo-mid: #6b4d3f;
    --photo-light: #c9a08a;
  }
  * { box-sizing: border-box; margin: 0; padding: 0; }
  html, body { width: 1200px; height: 900px; overflow: hidden; background: var(--page); }
  .canvas { position: relative; width: 1200px; height: 900px; }

  .card {
    position: absolute;
    left: 280px;
    width: 640px;
    height: 366px;
    border-radius: 22px;
    overflow: hidden;
    box-shadow: 0 10px 28px rgba(0,0,0,.22);
  }

  /* Back side */
  .card--back {
    top: 60px;
    background: linear-gradient(135deg, var(--card-black-soft) 0%, var(--card-black) 55%, #050505 100%);
    display: flex; flex-direction: column; align-items: center; justify-content: center;
  }
  .identity { text-align: center; }
  .identity__mark {
    display: block; width: 22px; height: 22px; margin: 0 auto 14px;
    background: var(--red);
  }
  .identity__name {
    font-family: "Questrial", sans-serif;
    font-size: 44px; color: var(--grey-light); line-height: 1; letter-spacing: .5px;
  }
  .identity__title {
    font-family: "Questrial", sans-serif;
    font-size: 26px; color: var(--red); line-height: 1.1; margin-top: 2px; letter-spacing: .5px;
  }

  /* Front side */
  .card--front { top: 470px; background: var(--white); }
  .front__bands { position: absolute; inset: 0; }

  .brokerage {
    position: absolute; left: 34px; top: 38px;
    display: flex; align-items: center; gap: 8px;
  }
  .brokerage__mark { width: 16px; height: 16px; background: var(--red); }
  .brokerage__name {
    font-family: "Arimo", sans-serif; font-weight: 700;
    font-size: 17px; color: var(--red);
  }
  .brokerage__url {
    position: absolute; left: 34px; top: 66px;
    font-family: "Arimo", sans-serif; font-weight: 700;
    font-size: 11px; color: var(--red);
  }

  .front__identity {
    position: absolute; left: 232px; top: 44px; width: 210px; text-align: center;
  }
  .front__identity .identity__mark { width: 18px; height: 18px; margin-bottom: 10px; }
  .front__identity .identity__name { font-size: 29px; color: var(--grey-name); letter-spacing: 0; }
  .front__identity .identity__title { font-size: 18px; }

  .portrait {
    position: absolute; right: 14px; top: 22px; width: 230px; height: 300px;
    background: radial-gradient(ellipse 55% 52% at 50% 48%, var(--photo-light) 0%, var(--photo-mid) 38%, var(--photo-dark) 68%, rgba(43,29,23,0) 100%);
  }

  .contact {
    position: absolute; left: 30px; top: 196px;
    font-family: "Arimo", sans-serif; font-size: 16px; color: var(--white);
    list-style: none;
  }
  .contact__item { display: flex; align-items: center; gap: 10px; height: 28px; white-space: nowrap; }
  .contact__item--indent { padding-left: 28px; margin-top: -4px; }
  .contact__icon { width: 18px; height: 18px; flex: none; fill: var(--white); }
  .contact__pair { display: flex; align-items: center; gap: 10px; margin-left: 18px; }
</style>
</head>
<body>
<main class="canvas">

  <section class="card card--back" aria-label="Business card, back">
    <div class="identity">
      <span class="identity__mark"></span>
      <p class="identity__name">Tessa Brandow</p>
      <p class="identity__title">WI &amp; MN Realtor</p>
    </div>
  </section>

  <section class="card card--front" aria-label="Business card, front">
    <svg class="front__bands" width="640" height="366" viewBox="0 0 640 366" aria-hidden="true">
      <defs>
        <linearGradient id="redBand" x1="0" y1="0" x2="1" y2="1">
          <stop offset="0" stop-color="#b8212f"/>
          <stop offset="1" stop-color="#8e1622"/>
        </linearGradient>
      </defs>
      <path d="M0 196 C 160 170, 330 168, 640 150 L640 160 C 330 178, 160 182, 0 206 Z" fill="#d4d4d6"/>
      <path d="M0 204 C 160 182, 330 178, 640 160 L640 366 L0 366 Z" fill="url(#redBand)"/>
    </svg>

    <div class="brokerage">
      <span class="brokerage__mark"></span>
      <span class="brokerage__name">Corvath Homes</span>
    </div>
    <p class="brokerage__url">www.corvathhomes.example</p>

    <div class="front__identity">
      <span class="identity__mark"></span>
      <p class="identity__name">Tessa Brandow</p>
      <p class="identity__title">WI &amp; MN Realtor</p>
    </div>

    <div class="portrait" role="img" aria-label="Portrait photograph of the agent, background removed"></div>

    <ul class="contact">
      <li class="contact__item">
        <svg class="contact__icon" viewBox="0 0 24 24"><path d="M12 2a7 7 0 0 0-7 7c0 5 7 13 7 13s7-8 7-13a7 7 0 0 0-7-7zm0 9.5A2.5 2.5 0 1 1 12 6.5a2.5 2.5 0 0 1 0 5z"/></svg>
        18632 County Lane 42/88 South
      </li>
      <li class="contact__item contact__item--indent">Dunmere, LK 61359</li>
      <li class="contact__item">
        <svg class="contact__icon" viewBox="0 0 24 24"><path d="M2 5h20v14H2z M3.5 6.5 12 13l8.5-6.5" fill="none" stroke="#fff" stroke-width="2"/></svg>
        TessaBrandow@CorvathHomes.example
      </li>
      <li class="contact__item">
        <svg class="contact__icon" viewBox="0 0 24 24"><path d="M7 2h10a1 1 0 0 1 1 1v18a1 1 0 0 1-1 1H7a1 1 0 0 1-1-1V3a1 1 0 0 1 1-1zm1 3v13h8V5zm4 14.2a1 1 0 1 0 0 2 1 1 0 0 0 0-2z"/></svg>
        555.204.6181
        <span class="contact__pair">
          <svg class="contact__icon" viewBox="0 0 24 24"><path d="M3 8c4-4 14-4 18 0l-2 3-4-1V8H9v2l-4 1zM6 12h12l2 8H4z"/></svg>
          555.862.1947
        </span>
      </li>
      <li class="contact__item">
        <svg class="contact__icon" viewBox="0 0 24 24"><path d="M7 3h8l2 2v5H7zM4 11h16a1 1 0 0 1 1 1v8H3v-8a1 1 0 0 1 1-1zm3 4v2h10v-2z"/></svg>
        555.862.4073
      </li>
    </ul>
  </section>

</main>
</body>
</html>
```